Business Card Design for a Jockey's Agent

A business card design that helps to develop a brand or identity for myself, the agent, perhaps on one side with a clean minimalist design, and on the other side a simple design with the two jockeys names i currently represent. Those jockeys may change twice a year as they move around the country, switch agents, etc, so i think keeping one side designed to promote the agent and a second side that can be changed easily to identify the jockeys i currently represent would be the best.

Target Market(s)

Thoroughbred racehorse trainers

Industry/Entity Type

Business

Contact Information for Business Card

Garrett Lindqvist - Jockey Agent
mobile (614) 382 7291
garrettplindqvist7mailhub.example

Jockeys: Everett Kline, Tobias Renwick

Font styles to use
Serif

Requirements
Must have
• contact info and modern feel and font
Nice to have
• clean minimalist element of racing, jockey silk, helmut or crop, finish marker pole from racetrack etc,
Should not have
• DONT HAVE ANY KIND OF LOGO ETC. IMAGE IS ONE OF MY RACEHORSES TO HELP FINISH BRIEF.
• racing horse, stuffy vintage racing feel or Weekly Paddock Sheet fonts

```html
<!DOCTYPE html>
<html lang="en">
<head>
<meta charset="utf-8">
<title>Garrett Lindqvist – Jockey Agent Business Card</title>
<link rel="stylesheet" href="https://fonts.googleapis.com/css2?family=Open+Sans:wght@400;600;700&display=swap">
<style>
  :root {
    --page-bg: #e6e8ea;
    --sky-blue: #2fb2e6;
    --deep-blue: #1a8dd6;
    --card-white: #ffffff;
    --swoosh-grey: #b9bcbf;
    --ink-grey: #4a4d50;
    --name-blue: #1b9ee0;
    --check-light: #cfeaf8;
  }
  * { margin: 0; padding: 0; box-sizing: border-box; }
  html, body {
    width: 1200px; height: 900px; overflow: hidden;
    background: var(--page-bg);
    font-family: "Open Sans", sans-serif;
  }
  .sheet {
    position: relative; width: 1200px; height: 900px;
    display: flex; flex-direction: column; align-items: center; justify-content: center; gap: 40px;
  }
  .card {
    position: relative; width: 630px; height: 360px; overflow: hidden;
    box-shadow: 0 6px 18px rgba(0,0,0,0.18);
  }

  /* Jockeys side */
  .card--jockeys {
    background: linear-gradient(100deg, var(--deep-blue) 0%, var(--sky-blue) 100%);
  }
  .card--jockeys .edge-strip {
    position: absolute; left: 0; width: 100%; background: var(--card-white);
  }
  .edge-strip--top { top: 0; height: 18px; }
  .edge-strip--bottom { bottom: 0; height: 12px; }
  .finish-band {
    position: absolute; left: 0; width: 100%;
    background: linear-gradient(90deg, var(--check-light), #8fd0f0 50%, var(--check-light));
  }
  .finish-band--top { top: 18px; height: 24px; }
  .finish-band--bottom { bottom: 12px; height: 30px; }
  .jockey-list {
    position: absolute; left: 0; right: 0; top: 150px;
    text-align: center; color: var(--card-white);
    font-weight: 600; font-size: 27px; letter-spacing: 0.3px;
  }

  /* Agent side */
  .card--agent { background: var(--card-white); }
  .card--agent .swoosh { position: absolute; inset: 0; }
  .agent-info {
    position: absolute; left: 0; right: 0; top: 112px; text-align: center;
    padding-left: 60px;
  }
  .agent-name {
    color: var(--name-blue); font-weight: 700; font-size: 30px; line-height: 1.1;
  }
  .agent-role {
    color: var(--ink-grey); font-size: 17px; margin-top: 2px;
  }
  .contact-row {
    position: absolute; left: 0; right: 0; top: 212px; padding-left: 60px;
    display: flex; justify-content: center; gap: 28px;
    color: var(--ink-grey); font-size: 15.5px;
  }
  .contact-item { display: flex; align-items: center; gap: 8px; }
  .contact-icon { color: var(--name-blue); font-weight: 700; }
</style>
</head>
<body>
<main class="sheet">
  <section class="card card--jockeys">
    <div class="edge-strip edge-strip--top"></div>
    <div class="finish-band finish-band--top" role="img" aria-label="Checkered finish-line band"></div>
    <p class="jockey-list">Jockeys: Everett Kline, Tobias Renwick</p>
    <div class="finish-band finish-band--bottom" role="img" aria-label="Checkered finish-line band"></div>
    <div class="edge-strip edge-strip--bottom"></div>
  </section>

  <section class="card card--agent">
    <svg class="swoosh" width="630" height="360" viewBox="0 0 630 360" aria-hidden="true">
      <defs>
        <linearGradient id="agentBlue" x1="0" y1="0" x2="1" y2="1">
          <stop offset="0" stop-color="#1a8dd6"/>
          <stop offset="1" stop-color="#38b6e8"/>
        </linearGradient>
        <linearGradient id="agentGrey" x1="0" y1="0" x2="0" y2="1">
          <stop offset="0" stop-color="#d6d8da"/>
          <stop offset="1" stop-color="#9fa3a6"/>
        </linearGradient>
      </defs>
      <rect width="630" height="360" fill="url(#agentBlue)"/>
      <ellipse cx="372" cy="124" rx="436" ry="262" fill="var(--card-white)"/>
      <ellipse cx="376" cy="120" rx="428" ry="254" fill="url(#agentGrey)"/>
      <ellipse cx="396" cy="112" rx="420" ry="250" fill="var(--card-white)"/>
    </svg>
    <div class="agent-info">
      <h1 class="agent-name">Garrett Lindqvist</h1>
      <p class="agent-role">Jockey Agent</p>
    </div>
    <div class="contact-row">
      <span class="contact-item">
        <svg class="contact-icon" width="12" height="12" viewBox="0 0 24 24" aria-hidden="true"><path fill="#1b9ee0" d="M6.6 10.8a15.1 15.1 0 0 0 6.6 6.6l2.2-2.2c.3-.3.7-.4 1-.2 1.1.4 2.3.6 3.6.6.6 0 1 .4 1 1V20c0 .6-.4 1-1 1C10.6 21 3 13.4 3 4c0-.6.4-1 1-1h3.5c.6 0 1 .4 1 1 0 1.3.2 2.5.6 3.6.1.3 0 .7-.2 1z"/></svg>
        (614) 382 7291
      </span>
      <span class="contact-item"><span class="contact-icon">@</span> garrettplindqvist7mailhub.example</span>
    </div>
  </section>
</main>
</body>
</html>
```